Lanternfield Voyages Business Card Design for Home Based Travel Agency

We already have a logo and I would like to see about getting a Business Card Design. The font on the logo can be changed. We are a home based travel agency and sell cruises and tour packages, etc. I would like the following information put into the design Name of Company and Tag Line from the logo. I would also like the email info@lanternfieldvoyages.example Phone 555-238-6140. Website www.lanternfieldvoyages.example. My name Neil Parton Travel Consultant and my wife's Name Mavis Parton. I would like you to use your imagination as nothing is off limites. Impress Me!

Target Market(s)

Baby Boomers

Industry/Entity Type

Travel Agent

Contact Information for Business Card

See above

Font styles to use
Serif
Sans Serif

Colors

Designer to choose colors to be used in the design.

Requirements
Must have
• Play with different fonts and needs to be easily readable, i.e. not too small of print.
Nice to have
• Use your imagination

```html
<!DOCTYPE html>
<html lang="en">
<head>
<meta charset="utf-8">
<title>Lanternfield Voyages – Business Cards</title>
<link href="https://fonts.googleapis.com/css2?family=Montserrat:ital,wght@1,300;1,400;1,700&family=Open+Sans:wght@300;400&display=swap" rel="stylesheet">
<style>
  :root {
    --green: #2aa84a;
    --red: #a01434;
    --blue: #2b8dd4;
    --orange: #f58634;
    --lime: #cfe11c;
    --charcoal: #444444;
    --ground: #3b3b3b;
    --ink: #ffffff;
    --shade: rgba(0, 0, 0, 0.5);
  }
  html, body { margin: 0; padding: 0; overflow: hidden; }
  .sheet {
    position: relative;
    width: 1200px;
    height: 1200px;
    background: var(--charcoal);
    overflow: hidden;
  }
  .divider {
    position: absolute;
    left: 0; top: 586px;
    width: 1200px; height: 28px;
    background: var(--ground);
  }
  .card { position: absolute; overflow: hidden; height: 293px; }
  .face { position: absolute; top: 0; width: 513px; height: 293px; color: var(--ink); text-align: center; }

  .is-green { background: var(--green); }
  .is-red { background: var(--red); }
  .is-blue { background: var(--blue); }
  .is-orange { background: var(--orange); }
  .is-lime { background: var(--lime); }
  .is-charcoal { background: var(--charcoal); }

  /* front */
  .brand-square {
    position: absolute; left: 216px; top: 40px;
    width: 80px; height: 80px;
    background: var(--ink);
  }
  .brand-name {
    position: absolute; left: 0; top: 168px; width: 100%;
    font-family: "Open Sans", sans-serif; font-weight: 300;
    font-size: 28px; line-height: 36px; letter-spacing: 4px; text-transform: uppercase;
    margin: 0;
  }
  .tagline {
    position: absolute; left: 0; top: 242px; width: 100%;
    font-family: "Open Sans", sans-serif; font-weight: 300;
    font-size: 15px; line-height: 20px; margin: 0;
  }

  /* back */
  .plane-art {
    position: absolute; left: 92px; top: 36px;
    width: 326px; height: 118px;
    background: var(--shade);
    border-radius: 0 60px 60px 0;
  }
  .names {
    position: absolute; left: 0; top: 116px; width: 100%;
    font-family: "Montserrat", sans-serif; font-style: italic; font-weight: 700;
    font-size: 23px; line-height: 30px; margin: 0;
  }
  .role {
    position: absolute; left: 0; top: 152px; width: 100%;
    font-family: "Montserrat", sans-serif; font-style: italic; font-weight: 400;
    font-size: 13px; line-height: 16px; margin: 0;
  }
  .contact {
    position: absolute; left: 0; top: 212px; width: 100%;
    font-family: "Montserrat", sans-serif; font-style: italic; font-weight: 300;
    font-size: 18px; line-height: 24px; margin: 0;
  }
  .contact span { display: block; }
</style>
</head>
<body>
<div class="sheet">
  <div class="divider"></div>

  <!-- top row fronts -->
  <div class="card is-green" style="left:0;top:0;width:343px">
    <div class="face" style="left:-20px">
      <div class="brand-square"></div>
      <p class="brand-name">Lanternfield Voyages</p>
      <p class="tagline">Every Journey is a Memory Worth Keeping</p>
    </div>
  </div>
  <div class="card is-blue" style="left:856px;top:0;width:344px">
    <div class="face" style="left:-148px">
      <div class="brand-square"></div>
      <p class="brand-name">Lanternfield Voyages</p>
      <p class="tagline">Every Journey is a Memory Worth Keeping</p>
    </div>
  </div>
  <div class="card is-red" style="left:343px;top:0;width:513px">
    <div class="face" style="left:0">
      <div class="brand-square"></div>
      <p class="brand-name">Lanternfield Voyages</p>
      <p class="tagline">Every Journey is a Memory Worth Keeping</p>
    </div>
  </div>

  <!-- second row fronts -->
  <div class="card is-orange" style="left:0;top:293px;width:513px">
    <div class="face" style="left:-20px">
      <div class="brand-square"></div>
      <p class="brand-name">Lanternfield Voyages</p>
      <p class="tagline">Every Journey is a Memory Worth Keeping</p>
    </div>
  </div>
  <div class="card is-lime" style="left:687px;top:293px;width:513px">
    <div class="face" style="left:21px">
      <div class="brand-square"></div>
      <p class="brand-name">Lanternfield Voyages</p>
      <p class="tagline">Every Journey is a Memory Worth Keeping</p>
    </div>
  </div>

  <!-- third row backs -->
  <div class="card is-lime" style="left:0;top:614px;width:513px">
    <div class="face" style="left:16px">
      <div class="plane-art" role="img" aria-label="Airplane silhouettes in flight"></div>
      <p class="names">Neil &amp; Mavis Parton</p>
      <p class="role">Travel Consultants</p>
      <p class="contact"><span>555-238-6140.</span><span>info@lanternfieldvoyages.example</span><span>www.lanternfieldvoyages.example.</span></p>
    </div>
  </div>
  <div class="card is-red" style="left:687px;top:614px;width:513px">
    <div class="face" style="left:17px">
      <div class="plane-art" role="img" aria-label="Airplane silhouettes in flight"></div>
      <p class="names">Neil &amp; Mavis Parton</p>
      <p class="role">Travel Consultants</p>
      <p class="contact"><span>555-238-6140.</span><span>info@lanternfieldvoyages.example</span><span>www.lanternfieldvoyages.example.</span></p>
    </div>
  </div>

  <!-- bottom row backs -->
  <div class="card is-orange" style="left:0;top:907px;width:343px">
    <div class="face" style="left:16px">
      <div class="plane-art" role="img" aria-label="Airplane silhouettes in flight"></div>
      <p class="names">Neil &amp; Mavis Parton</p>
      <p class="role">Travel Consultants</p>
      <p class="contact"><span>555-238-6140.</span><span>info@lanternfieldvoyages.example</span><span>www.lanternfieldvoyages.example.</span></p>
    </div>
  </div>
  <div class="card is-green" style="left:856px;top:907px;width:344px">
    <div class="face" style="left:-152px">
      <div class="plane-art" role="img" aria-label="Airplane silhouettes in flight"></div>
      <p class="names">Neil &amp; Mavis Parton</p>
      <p class="role">Travel Consultants</p>
      <p class="contact"><span>555-238-6140.</span><span>info@lanternfieldvoyages.example</span><span>www.lanternfieldvoyages.example.</span></p>
    </div>
  </div>
  <div class="card is-blue" style="left:343px;top:907px;width:513px">
    <div class="face" style="left:17px">
      <div class="plane-art" role="img" aria-label="Airplane silhouettes in flight"></div>
      <p class="names">Neil &amp; Mavis Parton</p>
      <p class="role">Travel Consultants</p>
      <p class="contact"><span>555-238-6140.</span><span>info@lanternfieldvoyages.example</span><span>www.lanternfieldvoyages.example.</span></p>
    </div>
  </div>

  <!-- centre feature card -->
  <div class="card is-charcoal" style="left:343px;top:411px;width:513px">
    <div class="face" style="left:0">
      <div class="brand-square"></div>
      <p class="brand-name">Lanternfield Voyages</p>
      <p class="tagline">Every Journey is a Memory Worth Keeping</p>
    </div>
  </div>
</div>
</body>
</html>
```